Korvex Systems*

Stationary design including business cards, letter heads, envelops and email signatures using our new logo

Target Market(s)

Innovative Technologies

Industry/Entity Type

Defense Contracting

Font styles to use
Sans Serif

```html
<!DOCTYPE html>
<html lang="en">
<head>
<meta charset="utf-8">
<title>Korvex Systems — Stationery</title>
<link rel="stylesheet" href="https://fonts.googleapis.com/css2?family=Oswald:wght@400;600&family=Poppins:wght@400&display=swap">
<style>
:root{
  --backdrop:#c8c8c8;
  --paper:#ffffff;
  --ink:#0b0c0d;
  --ink-soft:#2a2a2a;
  --shadow:0 2px 3px rgba(0,0,0,.35);
}
*{margin:0;padding:0;box-sizing:border-box}
html,body{width:1200px;height:1104px;overflow:hidden}
body{background:var(--backdrop);position:relative;font-family:"Poppins",sans-serif;color:var(--ink-soft)}
.piece{position:absolute;background:var(--paper);box-shadow:var(--shadow);overflow:hidden}
.brand{font-family:"Oswald",sans-serif;font-weight:400;color:var(--ink);white-space:nowrap;line-height:1;position:absolute;letter-spacing:-.2px}
.person-name{font-family:"Oswald",sans-serif;font-weight:600;color:var(--ink);text-transform:uppercase;line-height:1;position:absolute;white-space:nowrap}
.role{position:absolute;line-height:1;white-space:nowrap}
.address,.contacts{position:absolute;white-space:nowrap}
.contacts li{list-style:none;display:flex;align-items:center;gap:3px}
.icon{display:inline-block;flex:none}
.align-right{text-align:right}
.align-right li{justify-content:flex-end}

/* business card front */
.card-front{left:145px;top:69px;width:426px;height:245px}
.card-front .brand{left:24px;top:93px;font-size:20px}
.card-front .person-name{right:26px;top:109px;font-size:16px}
.card-front .role{right:26px;top:129px;font-size:10.5px}
.card-front .rule{position:absolute;left:24px;top:133px;width:279px;height:1.5px;background:var(--ink)}
.card-front .tab{position:absolute;right:0;top:110px;width:13px;height:27px;background:var(--ink)}
.card-front .address{left:24px;top:152px;font-size:10.5px;line-height:13.7px}
.card-front .contacts{left:24px;top:187px;font-size:10.5px;line-height:13.7px}

/* business card back */
.card-back{left:660px;top:69px;width:428px;height:245px;background:var(--ink)}
.card-back .brand{left:0;right:0;text-align:center;top:106px;font-size:28px;color:var(--paper)}

/* compliment slip */
.slip{left:69px;top:345px;width:547px;height:136px}
.slip .person-name{left:57px;top:20px;font-size:13px}
.slip .role{left:57px;top:38px;font-size:8.5px}
.slip .address{left:57px;top:60px;font-size:8.5px;line-height:11.5px}
.slip .contacts{left:57px;top:84px;font-size:8.5px;line-height:11.5px}
.slip .brand{right:56px;top:95px;font-size:20px}

/* envelope back */
.envelope-back{left:67px;top:511px;width:549px;height:252px}
.envelope-back .flap{position:absolute;left:0;top:0;width:549px;height:82px}

/* envelope front */
.envelope-front{left:66px;top:782px;width:548px;height:252px}
.envelope-front .brand{left:36px;top:84px;font-size:11px}
.envelope-front .address{left:36px;top:107px;font-size:7px;line-height:10px}
.envelope-front .contacts{left:36px;top:130px;font-size:7px;line-height:10px}

/* letterhead */
.letterhead{left:646px;top:345px;width:487px;height:690px}
.letterhead .brand{left:24px;top:71px;font-size:12px}
.letterhead .address{right:22px;top:22px;font-size:9px;line-height:12px}
.letterhead .contacts{right:22px;top:50px;font-size:9px;line-height:12px}
</style>
</head>
<body>

<svg width="0" height="0" style="position:absolute" aria-hidden="true">
  <defs>
    <symbol id="icon-phone" viewBox="0 0 10 10"><path d="M2 1l2 2-1 1.2a6 6 0 0 0 2.8 2.8L7 6l2 2-1.2 1.4C4.5 9.2.8 5.5.6 2.2z" fill="currentColor"/></symbol>
    <symbol id="icon-mail" viewBox="0 0 10 10"><rect x=".5" y="2" width="9" height="6.5" fill="currentColor"/><path d="M.8 2.4L5 5.6l4.2-3.2" stroke="#fff" stroke-width=".8" fill="none"/></symbol>
    <symbol id="icon-globe" viewBox="0 0 10 10"><circle cx="5" cy="5" r="4.5" fill="currentColor"/><path d="M3 2.5c1 .5 1.5 1.5 1 2.5s-1.5 1-1.5 2M6.5 3.5c1 0 1.5 1 2 1.5M6 8c.3-1 1-1.5 1.8-1.5" stroke="#fff" stroke-width=".8" fill="none"/></symbol>
  </defs>
</svg>

<section class="piece card-front" aria-label="Business card, front">
  <div class="brand">Korvex Systems</div>
  <div class="person-name">Daniel Hartwell</div>
  <div class="role">Executive Director</div>
  <div class="rule"></div>
  <div class="tab"></div>
  <p class="address">P.O. Box: 48210, Calder Row<br>London, United Kingdom</p>
  <ul class="contacts">
    <li><svg class="icon" width="9" height="9"><use href="#icon-phone"/></svg>+44 20 7946 0381</li>
    <li><svg class="icon" width="9" height="9"><use href="#icon-mail"/></svg>info@korvexsystems.com</li>
    <li><svg class="icon" width="9" height="9"><use href="#icon-globe"/></svg>www.korvexsystems.com</li>
  </ul>
</section>

<section class="piece card-back" aria-label="Business card, back">
  <div class="brand">Korvex Systems</div>
</section>

<section class="piece slip" aria-label="Compliment slip">
  <div class="person-name">Daniel Hartwell</div>
  <div class="role">Executive Director</div>
  <p class="address">P.O. Box: 48210, Calder Row<br>London, United Kingdom</p>
  <ul class="contacts">
    <li><svg class="icon" width="8" height="8"><use href="#icon-phone"/></svg>+44 20 7946 0381</li>
    <li><svg class="icon" width="8" height="8"><use href="#icon-mail"/></svg>info@korvexsystems.com</li>
    <li><svg class="icon" width="8" height="8"><use href="#icon-globe"/></svg>www.korvexsystems.com</li>
  </ul>
  <div class="brand">Korvex Systems</div>
</section>

<section class="piece envelope-back" aria-label="Envelope, back">
  <svg class="flap" viewBox="0 0 549 82" aria-hidden="true">
    <path d="M0 0H549L536 58C531 72 518 82 500 82H49C31 82 18 72 13 58Z" fill="var(--ink)"/>
  </svg>
</section>

<section class="piece envelope-front" aria-label="Envelope, front">
  <div class="brand">Korvex Systems</div>
  <p class="address">P.O. Box: 48210, Calder Row<br>London, United Kingdom</p>
  <ul class="contacts">
    <li><svg class="icon" width="6" height="6"><use href="#icon-phone"/></svg>+44 20 7946 0381</li>
    <li><svg class="icon" width="6" height="6"><use href="#icon-mail"/></svg>info@korvexsystems.com</li>
    <li><svg class="icon" width="6" height="6"><use href="#icon-globe"/></svg>www.korvexsystems.com</li>
  </ul>
</section>

<section class="piece letterhead" aria-label="Letterhead">
  <div class="brand">Korvex Systems</div>
  <p class="address align-right">P.O. Box: 48210, Calder Row<br>London, United Kingdom</p>
  <ul class="contacts align-right">
    <li>+44 20 7946 0381<svg class="icon" width="7" height="7"><use href="#icon-phone"/></svg></li>
    <li>info@korvexsystems.com<svg class="icon" width="7" height="7"><use href="#icon-mail"/></svg></li>
    <li>www.korvexsystems.com<svg class="icon" width="7" height="7"><use href="#icon-globe"/></svg></li>
  </ul>
</section>

</body>
</html>
```